Brellowin Redesign Website

Looking for a web design who can think out of the box.
Redesign of www.brellowin.com.au.
Design requirements:
- Use of many different Colors based on icon logo
- Use of nature and animal pictures that symbolize evolution, transition, metamorphosis, change, etc.
- Website background color for each page is based on Icon logo
- Website mood: Transition & Change, Water, Natural cycle, Waves, Natural evolution, Circle, Wheel,
- Landing page design with animated grafik based on logo icon
- Define colorful design flow that incorporates the website content (see attached file)
- Website development in Wix, access will be provided after final design

Target Market(s)

Non-for-profits in Health and Social sector, local small businesses

Industry/Entity Type

Community Development, Health, Aged-Care,

Coding

Coded - Design and coding required

Number of Pages Required

5+ page

Font styles to use
Sans Serif
Other font styles liked:
• MavenPro, Futura,

Colors
00AB8E
00BBA5
67D7C9
C6EFE9
E9F9F6
FFC000
F8CF3A
FAE287
FDF2CF
FEFAEE
F0912C
F2A743
F7CA91
FBE8D2
FDF5EE

Requirements
Must have
• Landing page with animated grafik, responsive design, out-of-box design, all pages and functions on current website, animated text and design ellements on all sides,
Nice to have
• use logo icon for landing page; it would be great if icon could be animated for the landing page, e.g. moving circles that coming out ot the head
Should not have
• look like a wix template, center aligments in block desciptions, corporate look

```html
<!DOCTYPE html>
<html lang="en">
<head>
<meta charset="utf-8">
<title>Brellowin</title>
<link href="https://fonts.googleapis.com/css2?family=Jost:wght@500;600;700&family=Maven+Pro:wght@400;500;600&display=swap" rel="stylesheet">
<style>
:root{
  --purple:#362058;
  --ink:#241446;
  --teal:#1f9fc2;
  --orange:#e8a33a;
  --yellow:#f9c867;
  --card:#bfe9f5;
  --grey-bg:#f5f4f8;
  --footer:#333333;
  --green:#5aa85a;
  --text:#2b2b2b;
}
*{margin:0;padding:0;box-sizing:border-box}
html,body{width:1200px;height:3652px;overflow:hidden}
body{position:relative;font-family:"Maven Pro",sans-serif;color:var(--text);background:#fff}
.abs{position:absolute}
.circle{position:absolute;border-radius:50%}
.photo{position:absolute}
h1,h2,.brand{font-family:"Jost",sans-serif}

/* hero */
.hero{position:absolute;left:0;top:0;width:1200px;height:505px;background:var(--purple);overflow:hidden}
.brand{color:#fff;font-weight:600;font-size:22px;display:flex;align-items:center;gap:8px}
.brand .dot{width:14px;height:14px;border-radius:50%;background:var(--orange)}
.nav{position:absolute;top:46px;left:610px;display:flex;gap:0;font-size:10px;letter-spacing:1px;color:#fff}
.nav a{color:#fff;text-decoration:none;position:absolute;white-space:nowrap}
.login{position:absolute;left:939px;top:38px;width:82px;height:29px;border:1.5px solid #fff;border-radius:3px;color:#fff;font-size:10px;letter-spacing:1px;font-weight:600;display:flex;align-items:center;justify-content:center}
.hero h1{position:absolute;left:0;width:1200px;top:155px;text-align:center;color:#fff;font-size:42px;line-height:48px;font-weight:700}
.hero h1 em{font-style:normal;color:var(--orange)}
.hero .sub{position:absolute;top:272px;width:1200px;text-align:center;color:#fff;font-size:17px}
.hero .author{position:absolute;top:314px;width:1200px;text-align:center;color:#fff;font-size:17px;font-weight:600;font-family:"Jost",sans-serif;letter-spacing:1px}

.heading{font-family:"Jost",sans-serif;font-weight:700;color:var(--ink);font-size:34px;line-height:40px;position:absolute;white-space:nowrap}
.kicker{position:absolute;font-size:12.5px;color:#222;white-space:nowrap}
.body{position:absolute;font-size:12.5px;line-height:25px;color:#333}
.body p{margin-bottom:4px}

/* cards */
.card{position:absolute;top:1655px;height:241px;width:210px;background:var(--card);border-radius:10px;overflow:hidden}
.card .thumb{position:absolute;left:12px;top:24px;width:186px;height:111px}
.card p{position:absolute;left:22px;top:152px;right:12px;font-size:12px;line-height:19.5px;letter-spacing:1px;color:#222;font-weight:500}
.pager{position:absolute;font-size:8px;letter-spacing:1px;color:#333}
.pager svg{display:block;margin-top:4px}

.grey{position:absolute;left:0;top:2006px;width:1200px;height:635px;background:var(--grey-bg);overflow:hidden}
.link{color:#5b4bb0}

.testimonial h2{position:absolute;top:2700px;width:1200px;text-align:center;font-size:33px;font-weight:700;color:var(--ink)}
.quote-text{position:absolute;left:270px;width:660px;top:2754px;text-align:center;font-size:15px;line-height:30px;color:#333}
.quotemark{position:absolute;left:228px;top:2712px;font-family:"Jost",sans-serif;font-size:80px;color:var(--green);font-weight:600;line-height:1}
.client{position:absolute;top:2866px;width:1200px;text-align:center;font-size:12px;color:#c39a6b}
.dots{position:absolute;top:2908px;left:584px;display:flex;gap:8px}
.dots span{width:4px;height:4px;border-radius:50%;background:#999}
.dots span.on{background:#333;width:5px;height:5px}

.footer{position:absolute;left:0;top:3454px;width:1200px;height:198px;background:var(--footer)}
.form-card{position:absolute;left:108px;top:2982px;width:986px;height:505px;background:#fff;box-shadow:0 4px 30px rgba(0,0,0,.06)}
.form-card h2{position:absolute;left:91px;top:72px;font-size:32px;font-weight:700;color:var(--ink)}
.form-card .lead{position:absolute;left:91px;top:135px;font-size:16px;color:#222}
.form-card .note{position:absolute;left:91px;top:168px;font-size:10px;line-height:21px;color:#333}
.field{position:absolute;width:383px;border-bottom:1px solid #e2e2e2;font-size:12.5px;color:#444;padding-bottom:12px}
.submit{position:absolute;left:92px;top:405px;width:109px;height:34px;border:2px solid var(--ink);font-size:11px;font-weight:600;display:flex;align-items:center;justify-content:center;color:#222}
.f-label{position:absolute;top:3543px;font-size:9px;color:var(--orange);font-weight:600}
.f-value{position:absolute;top:3561px;font-size:12.5px;color:#ddd}
</style>
</head>
<body>

<section class="hero">
  <svg class="abs" width="1200" height="505" style="left:0;top:0">
    <defs><linearGradient id="tri" x1="0" y1="1" x2="1" y2="0">
      <stop offset="0" stop-color="#1c5fa8"/><stop offset="1" stop-color="#1fa5c4"/></linearGradient></defs>
    <polygon points="692,505 1200,0 1200,505" fill="url(#tri)"/>
  </svg>
  <div class="circle" style="left:326px;top:-29px;width:100px;height:100px;background:#8e4aa8"></div>
  <div class="circle" style="left:785px;top:-35px;width:70px;height:55px;background:#d9a441"></div>
  <div class="circle" style="left:-6px;top:129px;width:34px;height:34px;background:#d9a441"></div>
  <div class="circle" style="left:259px;top:340px;width:50px;height:50px;background:#3a9ad9"></div>
  <div class="circle" style="left:-12px;top:449px;width:66px;height:66px;background:var(--green)"></div>
  <div class="circle" style="left:503px;top:432px;width:100px;height:100px;background:#2a5fa8"></div>
  <div class="circle" style="left:1157px;top:135px;width:84px;height:84px;background:#3cc3c9"></div>
  <div class="circle" style="left:891px;top:485px;width:48px;height:48px;background:#6cbf4e"></div>

  <div class="brand abs" style="left:160px;top:78px"><span class="dot"></span>Brellowin</div>
  <nav class="nav">
    <a href="#" style="left:0">HOME</a>
    <a href="#" style="left:73px">ABOUT</a>
    <a href="#" style="left:153px">SERVICE</a>
    <a href="#" style="left:238px">CONTACT</a>
  </nav>
  <div class="login">LOGIN</div>

  <h1>Yesterday I was clever, so<br>I wanted to <em>change</em> the world.</h1>
  <p class="sub">Today I am wise, so I am changing myself</p>
  <p class="author">- ORAVEN</p>
</section>

<!-- learnings -->
<div class="circle" style="left:-180px;top:827px;width:304px;height:304px;background:var(--yellow)"></div>
<div class="photo" role="img" aria-label="Wooden pier stretching across clear turquoise sea to a small wooded island" style="left:465px;top:569px;width:735px;height:394px;background:linear-gradient(180deg,#6fb2d6 0%,#9fd1e4 30%,#2d8fa3 55%,#1f6f7e 80%,#8a6a4d 100%)"></div>
<div class="circle" style="left:1124px;top:631px;width:100px;height:100px;background:rgba(122,196,140,.55)"></div>
<h2 class="heading" style="right:742px;top:696px">Our Learnings</h2>
<h2 class="heading" style="left:315px;top:742px">Over The Years</h2>
<p class="kicker" style="left:230px;top:802px">Technology Alone Won't Help You</p>
<div class="body" style="left:465px;top:987px;width:610px">
  <p>Fortunately or unfortunately, the shiny technology isn't a silver bullet you have been searching for. New technology can get you only so far. The challenge here is transforming the mindsets, behaviours with the new ways of working.</p>
  <p>Hence, the combination of these two will lead<br>to true organisational transformation. Improved performance is a combination of being effective, efficient, and technology.</p>
</div>

<!-- system review -->
<div class="photo" role="img" aria-label="Hiker resting on a rocky summit above hills at sunset" style="left:0;top:1213px;width:533px;height:475px;background:linear-gradient(180deg,#b9cbd6 0%,#f3d9a4 30%,#e7a04a 50%,#8a5a2b 72%,#3a2a1c 100%)"></div>
<div class="circle" style="left:-17px;top:1551px;width:76px;height:76px;background:#2f8fbf"></div>
<h2 class="heading" style="left:496px;top:1281px">Non-bios</h2>
<h2 class="heading" style="left:583px;top:1326px">System Review</h2>
<div class="body" style="left:583px;top:1381px;width:360px;color:#222">
  <p>Are You Looking into a Client Management System and Don't Know Where to Begin?</p>
</div>
<div class="body" style="left:583px;top:1463px;width:340px">
  <p>Our team does requirement workshops with your key staff members. Based on the requirements, we do a tool based agnostic research which is the best-fit solution for you, minus provider bios.</p>
  <p>We also provide a tool-based evaluation of best-fit systems; CRM or LMS or other systems. Non-bios.</p>
</div>
<div class="circle" style="left:1078px;top:1596px;width:340px;height:340px;background:var(--purple)"></div>

<div class="card" style="left:569px">
  <div class="thumb" role="img" aria-label="Penguins walking on a beach" style="background:linear-gradient(180deg,#c9d5dc,#8fa3ad 60%,#c2c5c2)"></div>
  <p>Find the best-fit Client Management System for your organisation without bios</p>
</div>
<div class="card" style="left:797px">
  <div class="thumb" role="img" aria-label="Butterfly emerging from chrysalises on a branch" style="background:linear-gradient(135deg,#a7c94a,#6f9a2c 60%,#4f6f22)"></div>
  <p style="top:171px">Identify change impact and resistance</p>
</div>
<div class="card" style="left:1025px;width:200px">
  <div class="thumb" role="img" aria-label="Mountain lake with a small village and reflections" style="background:linear-gradient(180deg,#b5d3e8,#5f8fa8 45%,#2e6f86 70%,#1c4a5c)"></div>
  <p style="top:171px">Automate your workflows</p>
</div>

<div class="pager" style="left:461px;top:1869px;color:#bbb">PREV
  <svg width="34" height="8"><path d="M1 4H33M1 4L5 1M1 4L5 7" stroke="#999" fill="none"/></svg></div>
<div class="pager" style="left:507px;top:1869px">NEXT
  <svg width="34" height="8"><path d="M1 4H33M33 4L29 1M33 4L29 7" stroke="#333" fill="none"/></svg></div>
<p class="abs" style="left:621px;top:1921px;font-size:13px;color:#222">View All</p>
<svg class="abs" style="left:696px;top:1916px" width="28" height="28"><circle cx="14" cy="14" r="13" fill="var(--green)"/><path d="M12 9l5 5-5 5" stroke="#fff" stroke-width="1.6" fill="none"/></svg>

<!-- committed -->
<section class="grey">
  <div class="circle" style="left:-184px;top:96px;width:298px;height:298px;background:var(--yellow)"></div>
</section>
<div class="photo" role="img" aria-label="Young elephant splashing water with two children in a misty river" style="left:654px;top:2077px;width:546px;height:476px;background:linear-gradient(160deg,#c9d49a 0%,#9aa963 35%,#6b7a40 65%,#4a4a2a 100%)"></div>
<div class="circle" style="left:1147px;top:2122px;width:104px;height:104px;background:rgba(63,190,170,.75)"></div>
<h2 class="heading" style="left:421px;top:2112px">We are</h2>
<h2 class="heading" style="left:525px;top:2159px">Committed</h2>
<p class="kicker" style="left:421px;top:2212px">To Our Local Community Support!</p>
<div class="body" style="left:235px;top:2269px;width:400px">
  <p>We are purpose and people-driven. Think of us as a safe pair of hands. We have a community fund that supports local NFP. I also volunteer as a business coach for women with Kindred Circle organisation: <span class="link">https://kindredcircle.org/</span></p>
  <p>We have extensive experience in working with government agencies and funding bodies. We have worked for aboriginal communities and organisations in northern territory.</p>
  <p>We are located in Byron Bay and provide also on-premises services to local NFPs in this region. We pride ourselves on our well-connected network of digital transformation and data experts in Australia and around the world, so our clients get the best-suited services and systems.</p>
</div>

<!-- testimonial -->
<section class="testimonial">
  <h2>What do Our Clients Have to Say?</h2>
  <div class="quotemark">“</div>
  <p class="quote-text">A rare breed of professionals who are both passionate and expert in their field. They are true professionals who truly understand the complexities of the change as well as the moving parts of complex projects.</p>
  <div class="pager" style="left:208px;top:2831px">PREV
    <svg width="32" height="8"><path d="M1 4H31M1 4L5 1M1 4L5 7" stroke="#333" fill="none"/></svg></div>
  <div class="pager" style="left:966px;top:2831px">NEXT
    <svg width="32" height="8"><path d="M1 4H31M31 4L27 1M31 4L27 7" stroke="#333" fill="none"/></svg></div>
  <p class="client">Maren T.</p>
  <div class="dots"><span></span><span class="on"></span><span></span></div>
</section>

<!-- footer -->
<footer class="footer"></footer>
<p class="f-label" style="left:337px">Phone :</p>
<p class="f-value" style="left:313px">+61400517284</p>
<p class="f-label" style="left:545px">Mail :</p>
<p class="f-value" style="left:476px;color:#aaa">getintouch@brellowin.com</p>
<p class="f-label" style="left:691px">Social Media :</p>
<p class="f-value" style="left:706px;color:#aaa">netlink</p>
<div class="brand abs" style="left:830px;top:3567px"><span class="dot"></span>Brellowin</div>
<p class="abs" style="left:843px;top:3608px;font-size:9.5px;color:#ddd">© 2022 Brellowin</p>

<!-- connect -->
<section class="form-card">
  <h2>Let’s Connect</h2>
  <p class="lead">Faced with a project that requires change management?</p>
  <p class="note">Simply fill out the form and our team will get back to you shortly. Not a fan of forms?<br>A call (+61400517284) or an email (getintouch@brellowin.com) will work too.</p>
  <div class="field" style="left:91px;top:227px">First Name</div>
  <div class="field" style="left:509px;top:227px">Last Name</div>
  <div class="field" style="left:92px;top:284px">Email</div>
  <div class="field" style="left:509px;top:284px">Phone *</div>
  <div class="field" style="left:92px;top:346px;width:800px">Message</div>
  <div class="submit">Submit</div>
</section>

</body>
</html>
```